Educational Agency in Abu Dhabi looking for an 8 pages website

We are looking for an 8 pages design for a website, we already have one but we need to refine it and it is www.brightcampuslink.ae - Please base it on logo colours (attached) I have uploaded our logo, website content logo colors to use it for the scheme.
We are looking for a smooth look and content added if possible, I also attached content and logo

Industry/Entity Type

Education

Coding

Coded - Design and coding required

Number of Pages Required

5+ page

```html
<!DOCTYPE html>
<html lang="en">
<head>
<meta charset="utf-8">
<title>Bright Campus – Study Abroad</title>
<link rel="stylesheet" href="https://fonts.googleapis.com/css2?family=Open+Sans:wght@400;600;700&display=swap">
<style>
:root{
  --navy:#1b2d63;
  --ink:#3a3a3a;
  --muted:#8a8a8a;
  --card:#efefef;
  --card-line:#d6d6d6;
  --white:#ffffff;
  --rule:#c9c9c9;
}
*{box-sizing:border-box;margin:0;padding:0}
html,body{width:1200px;height:2769px;overflow:hidden}
body{font-family:"Open Sans",Arial,sans-serif;color:var(--ink);background:var(--white);position:relative}
svg{display:block}
.topbar{height:37px;background:var(--navy);color:var(--white);display:flex;align-items:center;justify-content:space-between;padding:0 28px;font-size:17px}
.topbar .item{display:flex;align-items:center;gap:9px}
.topbar .right{display:flex;align-items:center}
.topbar .sep{width:1px;height:26px;background:rgba(255,255,255,.6);margin:0 26px}
.header{height:77px;display:flex;align-items:center;justify-content:space-between;padding:0 32px 0 26px}
.brand{display:flex;align-items:center;gap:10px;font-weight:700;font-size:20px;color:var(--navy);letter-spacing:.5px}
.brand .mark{width:30px;height:30px;background:var(--navy);border-radius:50%}
.header .tools{display:flex;align-items:center;gap:13px}
.search{width:246px;height:36px;border:1px solid #9a9a9a;display:flex;font-size:15px;color:#555}
.search span{flex:1;padding:7px 15px}
.search i{width:46px;border-left:1px solid #9a9a9a;display:flex;align-items:center;justify-content:center}
.contact-btn{height:36px;padding:0 28px;background:var(--navy);color:var(--white);font-size:15px;display:flex;align-items:center}
.nav{height:61px;background:var(--navy);display:flex;align-items:center;justify-content:space-between;padding:0 20px 0 29px;color:var(--white);font-size:17.2px;letter-spacing:-.1px}
.hero{height:549px;position:relative;background:linear-gradient(180deg,#41558b 0%,#3c5087 45%,#3b4f7e 62%,#3d5a5a 80%,#3a5247 100%)}
.hero blockquote{position:absolute;top:190px;left:0;right:0;text-align:center;color:var(--white);font-size:35px;line-height:40px}
.section-title{text-align:center;color:var(--navy);font-size:32px;font-weight:600;letter-spacing:1px}
.title-rule{width:278px;height:2px;background:var(--rule);margin:11px auto 0;position:relative}
.title-rule::after{content:"";position:absolute;left:50%;top:-2px;width:168px;height:5px;margin-left:-84px;background:var(--navy);border-radius:3px}
.lead{text-align:center;color:var(--muted);font-size:18px;line-height:28px;margin-top:24px}
.destinations{height:768px;position:relative;padding-top:46px;box-shadow:0 6px 6px -4px rgba(0,0,0,.25)}
.grid{position:absolute;left:126px;top:210px;width:950px;display:grid;grid-template-columns:repeat(3,310px);gap:16px 10px}
.country{height:231px;background:var(--card);border:1px solid var(--card-line);display:flex;flex-direction:column;align-items:center;padding-top:29px;font-size:19px;color:#555}
.country.active{background:var(--navy);border-color:var(--navy);color:var(--white)}
.country .badge{width:126px;height:126px;border-radius:50%;border:2px solid var(--navy);background:var(--white);display:flex;align-items:center;justify-content:center;margin-bottom:24px}
.country .flag{width:76px;height:34px;border-radius:3px}
.arrow{position:absolute;top:1130px;width:46px;height:46px}
.dots{position:absolute;left:0;right:0;top:724px;display:flex;justify-content:center;gap:4px}
.dots i{width:17px;height:17px;border-radius:50%;background:#a7a7a7}
.dots i.on{background:var(--navy)}
.why{height:576px;padding-top:50px;position:relative}
.features{position:absolute;left:85px;top:219px;width:1035px;display:grid;grid-template-columns:513px 513px;gap:9px 9px}
.feature{height:146px;background:var(--navy);color:var(--white);padding:17px 24px 0 55px;position:relative}
.feature svg{position:absolute;left:14px;top:15px}
.feature h3{font-size:16px;font-weight:600;line-height:20px;text-transform:uppercase}
.feature p{font-size:15px;line-height:20px;margin-top:9px}
.partners{height:262px;background:linear-gradient(120deg,#ececec,#dcdcdc 55%,#ededed);display:flex;align-items:center;padding-left:86px;gap:86px}
.partner{display:flex;align-items:center;gap:14px;font-size:24px;color:var(--navy);font-weight:600}
.partner .shape{width:64px;height:64px;background:var(--navy)}
.partner .shape.round{border-radius:50%}
.partner .shape.soft{background:#3d6fb5}
.footer{height:399px;background:var(--navy);color:var(--white);position:relative;font-size:18px}
.footer h4{font-size:18px;font-weight:400;position:absolute;top:68px;white-space:nowrap}
.footer .col-about{position:absolute;left:50px;top:0;width:380px}
.footer .col-about p{position:absolute;top:124px;line-height:23px;width:400px;white-space:nowrap}
.footer .col-about h5{position:absolute;top:217px;font-size:18px;font-weight:400;white-space:nowrap}
.social{position:absolute;top:260px;display:flex;gap:6px}
.social i{width:37px;height:37px;border:2px solid var(--white)}
.divider{position:absolute;top:88px;width:1px;height:250px;background:rgba(255,255,255,.4)}
.col-links{position:absolute;left:539px;top:0}
.col-links ul{position:absolute;top:118px;list-style:none;line-height:33.5px;width:200px}
.col-links li::before{content:"•";margin:0 10px 0 -6px}
.col-info{position:absolute;left:829px;top:0;width:320px}
.col-info ul{position:absolute;top:118px;list-style:none;line-height:35.5px;width:320px}
.col-info li{display:flex;align-items:center;gap:14px;white-space:nowrap}
.copyright{height:40px;background:#ececec;text-align:center;font-size:17px;line-height:40px;color:#222}
</style>
</head>
<body>
<div class="topbar">
  <div class="item">
    <svg width="18" height="18" viewBox="0 0 18 18"><circle cx="9" cy="9" r="7.5" fill="none" stroke="#fff" stroke-width="1.8"/><text x="9" y="13" text-anchor="middle" font-size="11" font-weight="700" fill="#fff" font-family="Arial">?</text></svg>
    Have you any question
  </div>
  <div class="right">
    <div class="item">
      <svg width="18" height="13" viewBox="0 0 18 13"><rect x="1" y="1" width="16" height="11" fill="none" stroke="#fff" stroke-width="1.5"/><path d="M1 1l8 6 8-6" fill="none" stroke="#fff" stroke-width="1.5"/></svg>
      info@brightcampuslink.edu
    </div>
    <span class="sep"></span>
    <div class="item">
      <svg width="14" height="16" viewBox="0 0 14 16"><path d="M3 1l3 3-2 2c1 2 3 4 5 5l2-2 3 3-2 2C6 14 0 8 1 3z" fill="#fff"/></svg>
      +9 5550-100-200
    </div>
  </div>
</div>

<header class="header">
  <div class="brand"><span class="mark"></span>BRIGHT CAMPUS</div>
  <div class="tools">
    <div class="search"><span>Search</span><i><svg width="14" height="14" viewBox="0 0 14 14"><circle cx="6" cy="6" r="4.5" fill="none" stroke="#777" stroke-width="1.4"/><path d="M9.5 9.5l3.5 3.5" stroke="#777" stroke-width="1.4"/></svg></i></div>
    <div class="contact-btn">CONTACT US</div>
  </div>
</header>

<nav class="nav">
  <span>HOME</span><span>ABOUT US</span><span>SERVICES</span><span>WHY STUDY ABROAD</span><span>STUDY DESTINATION</span><span>ENGLISH AND OTHER LANGUAGES</span><span>STUDY ONLINE</span><span>APPLY</span>
</nav>

<section class="hero" role="img" aria-label="Photo of a historic university building with students relaxing on the lawn, under a navy overlay">
  <blockquote>Education comes from within; you<br>get it by struggle and effort and thought.</blockquote>
</section>

<section class="destinations">
  <h2 class="section-title">STUDY DESTINATION</h2>
  <div class="title-rule"></div>
  <p class="lead">Lorem ipsum dolor sit amet, non nullam, eget in neque, consequat amet at nulla.<br>Arcu quis lobortis, velit nunc ac</p>
  <div class="grid">
    <div class="country"><div class="badge"><span class="flag" role="img" aria-label="Crossed flags of the UK" style="background:linear-gradient(90deg,#1f3b7a,#c8202f 50%,#1f3b7a)"></span></div>Flag icon of uk</div>
    <div class="country"><div class="badge"><span class="flag" role="img" aria-label="Crossed flags of the USA" style="background:linear-gradient(90deg,#c8202f,#e9e9f2 50%,#2a3d7d)"></span></div>Flag icon of usa</div>
    <div class="country"><div class="badge"><span class="flag" role="img" aria-label="Crossed flags of Australia" style="background:linear-gradient(90deg,#1f3b7a,#c8202f 50%,#1f3b7a)"></span></div>Flag icon of australia</div>
    <div class="country"><div class="badge"><span class="flag" role="img" aria-label="Crossed flags of New Zealand" style="background:linear-gradient(90deg,#1f3b7a,#c8202f 50%,#1f3b7a)"></span></div>Flag icon of zealand</div>
    <div class="country active"><div class="badge"><span class="flag" role="img" aria-label="Crossed flags of China" style="background:linear-gradient(90deg,#e0281e,#f05a24 50%,#e0281e)"></span></div>Flag icon of china</div>
    <div class="country"><div class="badge"><span class="flag" role="img" aria-label="Crossed flags of Germany" style="background:linear-gradient(180deg,#222 0 33%,#d4181f 33% 66%,#f4c20d 66%)"></span></div>Flag icon of germany</div>
  </div>
  <div class="dots"><i class="on"></i><i></i><i class="on"></i><i></i></div>
</section>
<svg class="arrow" style="left:33px" viewBox="0 0 46 46"><circle cx="23" cy="23" r="22" fill="#fff" stroke="#1b2d63" stroke-width="2"/><path d="M26 15l-8 8 8 8" fill="none" stroke="#1b2d63" stroke-width="2.5"/></svg>
<svg class="arrow" style="left:1117px" viewBox="0 0 46 46"><circle cx="23" cy="23" r="22" fill="#fff" stroke="#1b2d63" stroke-width="2"/><path d="M20 15l8 8-8 8" fill="none" stroke="#1b2d63" stroke-width="2.5"/></svg>

<section class="why">
  <h2 class="section-title">WHY BRIGHT CAMPUS</h2>
  <div class="title-rule"></div>
  <p class="lead">Lorem ipsum dolor sit amet, non nullam, eget in neque, consequat amet at nulla.<br>Arcu quis lobortis, velit nunc ac</p>
  <div class="features">
    <article class="feature">
      <svg width="32" height="32" viewBox="0 0 32 32"><circle cx="16" cy="16" r="15" fill="#fff"/><circle cx="16" cy="12" r="5" fill="#1b2d63"/><path d="M7 25c2-6 16-6 18 0z" fill="#1b2d63"/></svg>
      <h3>Experienced counselling and advice based<br>on you</h3>
      <p>Experienced counselors available to help you identify the<br>best education plan for you!</p>
    </article>
    <article class="feature">
      <svg width="32" height="32" viewBox="0 0 32 32"><circle cx="16" cy="16" r="15" fill="#fff"/><path d="M8 10c4-1 6 2 5 5s-4 2-3 6M20 6c-1 4 3 5 6 4M19 26c0-4 3-5 6-6" fill="none" stroke="#1b2d63" stroke-width="3"/></svg>
      <h3>Wide range of countries</h3>
      <p>From China East to Canada West, going through USA, UK, Europe and more. We can help you decide which country is the most suitable for you based on your circumstances.</p>
    </article>
    <article class="feature">
      <svg width="32" height="32" viewBox="0 0 32 32"><circle cx="16" cy="7" r="5" fill="#fff"/><path d="M2 13l14 4 14-4v15l-14 4-14-4z" fill="#fff"/></svg>
      <h3>Partnerships with a global network of universities and educational institutions</h3>
      <p>We officially collaborate with over 300 domestic and international accredited educational institutions to ensure you get the best quality</p>
    </article>
    <article class="feature">
      <svg width="32" height="32" viewBox="0 0 32 32"><rect x="5" y="4" width="22" height="27" rx="2" fill="#fff"/><rect x="11" y="1" width="10" height="6" rx="1" fill="#fff" stroke="#1b2d63" stroke-width="1.5"/><path d="M10 14h12M10 19h12M10 24h8" stroke="#1b2d63" stroke-width="2"/></svg>
      <h3>Registration and accreditation</h3>
      <p>Registered with the Regional Council for Learning Standards. We are also members of multiple quality assurance and global educational associations.</p>
    </article>
  </div>
</section>

<section class="partners">
  <div class="partner"><span class="shape soft"></span>Northgate Partners</div>
  <div class="partner"><span class="shape round"></span>Vantex Council</div>
  <div class="partner"><span class="shape"></span>Civic Board of Learning</div>
</section>

<footer class="footer">
  <div class="col-about">
    <h4>ABOUT BRIGHT CAMPUS</h4>
    <p>Lorem ipsum dolor sit amet, non nullam,<br>eget in neque, consequat amet at nulla.<br>Arcu quis lobortis, velit nunc ac</p>
    <h5>FOLLOW US</h5>
    <div class="social"><i></i><i></i><i></i><i></i><i></i></div>
  </div>
  <span class="divider" style="left:467px"></span>
  <div class="col-links">
    <h4>FEATURE LINKS</h4>
    <ul><li>Graduation</li><li>Courses</li><li>Admission</li><li>International</li><li>Book store</li><li>FAQ</li></ul>
  </div>
  <span class="divider" style="left:762px"></span>
  <div class="col-info">
    <h4>INFORMATION</h4>
    <ul>
      <li><svg width="18" height="16" viewBox="0 0 18 16"><path d="M9 1L1 8h2v7h4v-4h4v4h4V8h2z" fill="#fff"/></svg>12 harbor learning street</li>
      <li><svg width="18" height="16" viewBox="0 0 14 16"><path d="M3 1l3 3-2 2c1 2 3 4 5 5l2-2 3 3-2 2C6 14 0 8 1 3z" fill="#fff"/></svg>+9 5550-100-200</li>
      <li><svg width="18" height="13" viewBox="0 0 18 13"><rect x="1" y="1" width="16" height="11" fill="none" stroke="#fff" stroke-width="1.5"/><path d="M1 1l8 6 8-6" fill="none" stroke="#fff" stroke-width="1.5"/></svg>info@brightcampuslink.edu</li>
      <li><svg width="18" height="16" viewBox="0 0 18 16"><path d="M1 6c4-5 12-5 16 0l-3 2-2-2H6L4 8zM4 9h10l1 6H3z" fill="#fff"/></svg>555-010-777</li>
    </ul>
  </div>
</footer>
<div class="copyright">copyright2018brightcampus</div>
</body>
</html>
```